Now Leasing Banner

Looking for a banner that says the following information approx 4' x 30'

Now Leasing Maplewood Terrace 925-318-6054

Target Market(s)

Drive by traffic

Industry/Entity Type

Residential property management

Requirements
Must have
• Clear and readable from a distance

```html
<!DOCTYPE html>
<html lang="en">
<head>
<meta charset="UTF-8">
<title>Now Leasing – Maplewood Terrace</title>
<link rel="stylesheet" href="https://fonts.googleapis.com/css2?family=Barlow+Condensed:wght@700&family=Barlow+Semi+Condensed:wght@700&display=swap">
<style>
  :root {
    --banner-blue: #3b55a6;
    --call-red: #e81c24;
    --text-white: #ffffff;
  }
  html, body {
    margin: 0;
    padding: 0;
    overflow: hidden;
    background: var(--banner-blue);
  }
  .banner {
    position: relative;
    width: 1200px;
    height: 160px;
    background: var(--banner-blue);
    overflow: hidden;
  }
  .headline {
    position: absolute;
    left: 33px;
    top: 14px;
    margin: 0;
    font-family: "Barlow Condensed", "Arial Narrow", sans-serif;
    font-weight: 700;
    font-size: 70px;
    line-height: 67px;
    letter-spacing: 0.5px;
    color: var(--text-white);
    text-transform: uppercase;
  }
  .headline span {
    display: block;
  }
  .phone-pill {
    position: absolute;
    left: 619px;
    top: 22px;
    width: 640px;
    height: 113px;
    box-sizing: border-box;
    border: 5px solid var(--text-white);
    border-radius: 57px;
    background: var(--call-red);
  }
  .phone-number {
    position: absolute;
    left: 42px;
    top: 0;
    width: 520px;
    height: 103px;
    display: flex;
    align-items: center;
    justify-content: center;
    margin: 0;
    font-family: "Barlow Semi Condensed", "Arial Narrow", sans-serif;
    font-weight: 700;
    font-size: 76px;
    letter-spacing: 1px;
    color: var(--text-white);
  }
</style>
</head>
<body>
  <div class="banner">
    <h1 class="headline">
      <span class="headline-line">Now Leasing</span>
      <span class="headline-line">Maplewood Terrace</span>
    </h1>
    <div class="phone-pill">
      <p class="phone-number">925-318-6054</p>
    </div>
  </div>
</body>
</html>
```